Please Help us Design a Tradeshow Banner

We need to design a banner that is 33 x 86. We do IT services. We want a tradeshow banner that will help us to stand out.

Target Market(s)

We are targeting small and medium sized businesses for trade shows.

Industry/Entity Type

IT Services

Font styles to use
Other font styles liked:
• Myriad Pro

Colors
FFC000
F8CF3A
FAE287
FDF2CF
FEFAEE

Requirements
Must have
• Our company's name and logo.
Nice to have
• Something that stands out but still looks professional.

```html
<!DOCTYPE html>
<html lang="en">
<head>
<meta charset="utf-8">
<title>Vantrel IT Services – Tradeshow Banner</title>
<link href="https://fonts.googleapis.com/css2?family=PT+Sans+Narrow:wght@700&family=PT+Sans:wght@700&family=Source+Sans+3:wght@700&display=swap" rel="stylesheet">
<style>
  :root {
    --gold: #ffc000;
    --amber: #f5a71c;
    --amber-deep: #e8900a;
    --sun: #f8cf3a;
    --cream: #fae287;
    --paper: #ececec;
    --ink: #111111;
    --copper: #cc7a3f;
    --sky: #8ec6e6;
    --night: #1d2430;
  }
  html, body { margin: 0; padding: 0; overflow: hidden; }
  body { width: 1200px; height: 3127px; background: var(--paper); }
  .banner { position: relative; width: 1200px; height: 3127px; overflow: hidden; background: var(--paper); font-family: "PT Sans Narrow", "Arial Narrow", sans-serif; color: var(--ink); }
  .shapes { position: absolute; inset: 0; }
  .hero-photo { position: absolute; inset: 0; }
  .brand { position: absolute; left: 138px; top: 150px; color: #fff; text-align: right; width: 320px; }
  .brand-name { font-family: "PT Sans", sans-serif; font-weight: 700; font-size: 78px; line-height: 1; display: block; letter-spacing: -1px; }
  .brand-sub { font-family: "PT Sans", sans-serif; font-weight: 700; font-size: 38px; line-height: 1.1; display: block; padding-right: 70px; }
  .headline { position: absolute; left: 0; width: 1200px; top: 578px; margin: 0; text-align: center; color: #fff; font-size: 118px; font-weight: 700; line-height: 1; text-shadow: 0 4px 10px rgba(0,0,0,.85), 0 0 3px #000; letter-spacing: -1px; }
  .intro { position: absolute; left: 74px; top: 1180px; margin: 0; font-size: 42px; line-height: 44px; width: 700px; }
  .pitch { position: absolute; left: 74px; top: 1352px; margin: 0; font-size: 42px; line-height: 43px; width: 960px; }
  .section-title { position: absolute; left: 0; width: 1200px; margin: 0; text-align: center; font-size: 56px; font-weight: 700; line-height: 1; }
  .focus-title { top: 1592px; }
  .services-title { top: 1968px; }
  .item { position: absolute; transform: translateX(-50%); text-align: center; }
  .item svg { display: block; margin: 0 auto; }
  .focus-item .label { font-family: "PT Sans", sans-serif; font-size: 27px; line-height: 35px; margin-top: 28px; color: #222; }
  .service-item .label { font-family: "Source Sans 3", sans-serif; font-size: 38px; line-height: 50px; margin-top: 54px; color: var(--sky); white-space: nowrap; }
  .web { position: absolute; left: 388px; top: 2765px; display: flex; align-items: center; gap: 46px; }
  .web-url { font-size: 56px; font-weight: 700; line-height: 1; }
</style>
</head>
<body>
<div class="banner">
  <svg class="hero-photo" width="1200" height="1200" viewBox="0 0 1200 1200" role="img" aria-label="Photo of a businessman in a dark suit holding a tablet, with a world map and network of connected people overlaid">
    <defs>
      <linearGradient id="heroTone" x1="0" y1="0" x2="0" y2="1">
        <stop offset="0" stop-color="#2a2e36"/>
        <stop offset=".55" stop-color="#343b48"/>
        <stop offset="1" stop-color="#1b2029"/>
      </linearGradient>
      <radialGradient id="heroGlow" cx=".55" cy=".78" r=".3">
        <stop offset="0" stop-color="#4c86d6" stop-opacity=".7"/>
        <stop offset="1" stop-color="#4c86d6" stop-opacity="0"/>
      </radialGradient>
    </defs>
    <polygon points="0,0 1200,0 1200,1062 886,1199 0,834" fill="url(#heroTone)"/>
    <polygon points="0,0 1200,0 1200,1062 886,1199 0,834" fill="url(#heroGlow)"/>
  </svg>

  <svg class="shapes" width="1200" height="3127" viewBox="0 0 1200 3127" aria-hidden="true">
    <polygon points="0,762 250,905 288,1030 0,885" fill="var(--amber)"/>
    <polygon points="0,790 236,903 258,978 0,850" fill="var(--amber-deep)"/>
    <line x1="312" y1="946" x2="484" y2="1024" stroke="var(--amber-deep)" stroke-width="9"/>
    <line x1="484" y1="1008" x2="886" y2="1196" stroke="var(--amber)" stroke-width="9"/>
    <polygon points="1200,1062 795,1272 1200,1466" fill="var(--amber)"/>
    <polygon points="0,2938 668,2938 860,3127 0,3127" fill="var(--amber)"/>
    <polygon points="560,2938 668,2938 860,3127 760,3127" fill="var(--sun)"/>
    <polygon points="700,2990 1200,2990 1200,3127 840,3127" fill="#ffc64a"/>
    <rect x="0" y="3090" width="1200" height="37" fill="var(--gold)" opacity=".6"/>
  </svg>

  <div class="brand">
    <span class="brand-name">Vantrel</span>
    <span class="brand-sub">IT Services</span>
  </div>

  <h1 class="headline">You DESERVE Better</h1>

  <p class="intro">Work with a team of technologists that are, well, simply better.</p>
  <p class="pitch">Vantrel knows what a critical role technology plays in your business, and that’s why you need a partner that approaches IT services differently. Haven’t you ever felt like IT should just be less of a hassle and more of an asset? So do we.</p>

  <h2 class="section-title focus-title">Our core focus</h2>

  <div class="item focus-item" style="left:169px;top:1718px">
    <svg width="104" height="100" viewBox="0 0 104 100"><path d="M12 60 V46 a40 40 0 0 1 80 0 V60" fill="none" stroke="var(--copper)" stroke-width="12"/><rect x="4" y="48" width="24" height="34" rx="10" fill="var(--copper)"/><rect x="76" y="48" width="24" height="34" rx="10" fill="var(--copper)"/><path d="M88 80 q0 14 -24 14 h-10" fill="none" stroke="var(--copper)" stroke-width="7"/><rect x="40" y="88" width="18" height="11" rx="5" fill="var(--copper)"/></svg>
    <div class="label">IT Support</div>
  </div>
  <div class="item focus-item" style="left:384px;top:1718px">
    <svg width="104" height="100" viewBox="0 0 104 100"><path d="M6 0 V92 H100" fill="none" stroke="var(--copper)" stroke-width="7"/><rect x="22" y="48" width="8" height="36" fill="var(--copper)"/><rect x="40" y="60" width="8" height="24" fill="var(--copper)"/><rect x="58" y="34" width="8" height="50" fill="var(--copper)"/><rect x="76" y="18" width="8" height="66" fill="var(--copper)"/></svg>
    <div class="label">Managed<br>Services</div>
  </div>
  <div class="item focus-item" style="left:623px;top:1706px">
    <svg width="92" height="92" viewBox="0 0 92 92"><rect x="0" y="0" width="92" height="92" fill="var(--copper)"/></svg>
    <div class="label" style="margin-top:40px">Platform<br>Consulting</div>
  </div>
  <div class="item focus-item" style="left:827px;top:1716px">
    <svg width="96" height="102" viewBox="0 0 96 102"><path d="M48 4 L92 18 V48 C92 76 72 92 48 100 C24 92 4 76 4 48 V18 Z" fill="var(--copper)"/><path d="M48 16 L80 26 V48 C80 68 66 80 48 87 Z" fill="var(--paper)"/></svg>
    <div class="label">Security</div>
  </div>
  <div class="item focus-item" style="left:1036px;top:1724px">
    <svg width="126" height="88" viewBox="0 0 126 88"><path d="M28 88 A26 26 0 0 1 26 36 A34 34 0 0 1 90 28 A30 30 0 0 1 98 88 Z" fill="var(--copper)"/></svg>
    <div class="label">Cloud Hosting</div>
  </div>

  <h2 class="section-title services-title">Our IT Services</h2>

  <div class="item service-item" style="left:271px;top:2092px">
    <svg width="100" height="90" viewBox="0 0 100 90"><path d="M36 30 C22 18 26 2 38 4 C44 5 46 10 48 12 C50 10 52 5 58 4 C70 2 74 18 60 30 L48 40 Z" fill="var(--sky)"/><path d="M0 60 h20 l16 -8 h26 a6 6 0 0 1 0 12 h-18 h22 l22 -16 a7 7 0 0 1 10 10 L72 86 H0 Z" fill="var(--sky)"/></svg>
    <div class="label">Credit Union<br>IT Services</div>
  </div>
  <div class="item service-item" style="left:590px;top:2100px">
    <svg width="108" height="82" viewBox="0 0 108 82"><path d="M6 30 a68 68 0 0 1 96 0" fill="none" stroke="var(--sky)" stroke-width="10" stroke-linecap="round"/><path d="M24 48 a42 42 0 0 1 60 0" fill="none" stroke="var(--sky)" stroke-width="10" stroke-linecap="round"/><circle cx="54" cy="72" r="10" fill="var(--sky)"/></svg>
    <div class="label">WiFi Network<br>Solutions</div>
  </div>
  <div class="item service-item" style="left:908px;top:2092px">
    <svg width="110" height="76" viewBox="0 0 110 76"><path d="M24 76 A22 22 0 0 1 22 32 A30 30 0 0 1 78 24 A26 26 0 0 1 86 76 Z" fill="var(--sky)"/></svg>
    <div class="label" style="margin-top:40px">Cloud &amp;<br>IT Strategies</div>
  </div>

  <div class="item service-item" style="left:261px;top:2410px">
    <svg width="108" height="90" viewBox="0 0 108 90"><rect x="40" y="0" width="28" height="22" rx="4" fill="var(--sky)"/><path d="M54 22 V40 M16 62 V40 H92 V62 M54 40 V62" fill="none" stroke="var(--sky)" stroke-width="7"/><rect x="2" y="62" width="28" height="24" rx="4" fill="var(--sky)"/><rect x="40" y="62" width="28" height="24" rx="4" fill="var(--sky)"/><rect x="78" y="62" width="28" height="24" rx="4" fill="var(--sky)"/></svg>
    <div class="label">Infrastructure<br>Upgrades</div>
  </div>
  <div class="item service-item" style="left:590px;top:2418px">
    <svg width="110" height="92" viewBox="0 0 110 92"><circle cx="55" cy="6" r="6" fill="var(--sky)"/><rect x="51" y="8" width="8" height="14" fill="var(--sky)"/><rect x="14" y="22" width="82" height="66" rx="16" fill="var(--sky)"/><rect x="0" y="40" width="10" height="30" rx="4" fill="var(--sky)"/><rect x="100" y="40" width="10" height="30" rx="4" fill="var(--sky)"/><circle cx="38" cy="46" r="7" fill="var(--paper)"/><circle cx="72" cy="46" r="7" fill="var(--paper)"/><path d="M38 70 h8 M51 70 h8 M64 70 h8" stroke="var(--paper)" stroke-width="4"/></svg>
    <div class="label">Monitoring &amp;<br>Automation</div>
  </div>
  <div class="item service-item" style="left:916px;top:2410px">
    <svg width="98" height="90" viewBox="0 0 98 90"><rect x="18" y="0" width="78" height="56" rx="6" fill="var(--sky)" opacity=".8"/><rect x="38" y="22" width="60" height="42" rx="4" fill="var(--sky)"/><rect x="0" y="34" width="68" height="56" rx="6" fill="var(--sky)"/><path d="M4 40 L34 66 L64 40" fill="none" stroke="var(--paper)" stroke-width="5"/></svg>
    <div class="label">Email<br>Management</div>
  </div>

  <div class="web">
    <svg width="62" height="62" viewBox="0 0 62 62"><circle cx="31" cy="31" r="31" fill="var(--ink)"/><g fill="none" stroke="#fff" stroke-width="3"><circle cx="31" cy="31" r="17"/><ellipse cx="31" cy="31" rx="7" ry="17"/><path d="M14 31 H48 M17 22 H45 M17 40 H45"/></g></svg>
    <span class="web-url">www.vantrel-it.com</span>
  </div>
</div>
</body>
</html>
```